We need a Word Template for Custom Laboratory Results from an independent laboratory

The test is a novel biomarker for a chronic pain condition called endometriosis. It is expressed as a percentage. We will upload a sample result. We are looking for improved graphic fidelity with more attention to design and spacing. Emphasis should be placed on the overall result, i.e. the patient percentage results. Considerationis going to be given to the most appealing graphic result.

Target Market(s)

Women aged 19-45

Colors
0054AA
0677BA
7BADD7
CADEEF
E8F1F8

```html
<!DOCTYPE html>
<html lang="en">
<head>
<meta charset="utf-8">
<title>Endosigna Micro-RNA Endometriosis Assay – Results</title>
<link rel="stylesheet" href="https://fonts.googleapis.com/css2?family=Open+Sans:wght@400;600;700&display=swap">
<style>
  :root {
    --page: #ffffff;
    --brand-teal: #2a8c9a;
    --brand-navy: #2f55a4;
    --title-blue: #0677BA;
    --band-blue: #0672A6;
    --name-teal: #1a7aa8;
    --muted: #8a8a8a;
    --ink: #2a2a2a;
    --panel-left: #e4f7fc;
    --panel-right: #cdeff5;
    --ring-dark: #555a5e;
    --ring-accent: #19b6e8;
    --table-line: #2a7fbf;
    --row-neutral: #f5faf0;
    --row-alert: #fcebe4;
    --rule: #555555;
    --mark-fill: #8fc4cc;
    --backdrop-circle: #eef6f8;
  }
  * { box-sizing: border-box; margin: 0; padding: 0; }
  html, body { width: 1200px; height: 1000px; overflow: hidden; background: var(--page); }
  body { font-family: "Open Sans", Verdana, sans-serif; position: relative; }

  .backdrop-circle { position: absolute; left: 638px; top: 672px; width: 226px; height: 226px;
    border-radius: 50%; background: var(--backdrop-circle); }

  .report { position: absolute; left: 330px; top: 0; width: 541px; height: 1000px; }

  .masthead { position: absolute; top: 0; left: 0; width: 541px; height: 170px; }
  .clinic-mark { position: absolute; left: 1px; top: 94px; width: 56px; height: 56px; border-radius: 50%;
    background: var(--mark-fill); }
  .clinic-name { position: absolute; left: 96px; color: var(--brand-teal); font-weight: 400; white-space: nowrap; }
  .clinic-name.primary { top: 89px; font-size: 28px; line-height: 36px; letter-spacing: -0.3px; }
  .clinic-name.secondary { top: 130px; font-size: 15px; line-height: 20px; }
  .masthead-rule { position: absolute; left: 80px; right: 2px; top: 127px; height: 2px; background: var(--rule); }
  .lab-name { position: absolute; right: 2px; top: 132px; font-size: 21px; line-height: 28px; font-weight: 700; color: var(--brand-navy); }

  .assay-title { position: absolute; top: 192px; left: 0; width: 540px; text-align: center;
    color: var(--title-blue); font-size: 19.5px; font-weight: 700; line-height: 24px; letter-spacing: 0.2px; }

  .results-band { position: absolute; top: 258px; left: 1px; width: 539px; height: 30px; background: var(--band-blue);
    color: #fff; font-size: 12px; font-weight: 600; text-align: center; line-height: 30px; letter-spacing: 0.3px; }

  .patient { position: absolute; top: 299px; left: 0; }
  .patient-name { font-size: 15px; color: var(--name-teal); line-height: 20px; }
  .patient-meta { font-size: 11px; color: var(--muted); line-height: 14px; letter-spacing: 0.3px; }

  .score { position: absolute; top: 352px; left: 1px; width: 540px; height: 133px; display: flex; }
  .score-label { width: 270px; background: var(--panel-left); padding: 40px 0 0 18px;
    font-size: 11px; line-height: 12.5px; color: var(--muted); letter-spacing: 0.3px; }
  .score-value { flex: 1; background: var(--panel-right); display: flex; align-items: center; padding-left: 54px; gap: 22px; }
  .score-figure { font-size: 29px; font-weight: 700; color: var(--ink); letter-spacing: 0.6px; }

  .range-heading { position: absolute; top: 495px; left: 0; width: 540px; text-align: center;
    font-size: 11px; font-weight: 700; color: var(--ink); letter-spacing: 0.3px; }

  .range-table { position: absolute; top: 527px; left: 1px; width: 539px; border-collapse: collapse;
    font-size: 11px; color: #6a6a6a; letter-spacing: 0.3px; }
  .range-table td { border: 1px solid #2a7fbf; height: 20px; padding: 0 6px; }
  .range-table td.band { width: 92px; }
  .range-table tr.inconclusive td { background: var(--row-neutral); }
  .range-table tr.high td { background: var(--row-alert); }
</style>
</head>
<body>
  <div class="backdrop-circle" aria-hidden="true"></div>

  <main class="report">
    <header class="masthead">
      <div class="clinic-mark" aria-hidden="true"></div>
      <div class="clinic-name primary">Lumen</div>
      <div class="masthead-rule"></div>
      <div class="clinic-name secondary">Fertility Clinic</div>
      <div class="lab-name">Veridia</div>
    </header>

    <h1 class="assay-title">ENDOSIGNA MICRO-RNA<br>ENDOMETRIOSIS ASSAY</h1>

    <div class="results-band">YOUR RESULTS</div>

    <section class="patient">
      <div class="patient-name">Marin Okafor</div>
      <div class="patient-meta">OHIP: 1234567890123</div>
      <div class="patient-meta">DOB: 12th Jan. 2011</div>
    </section>

    <section class="score">
      <div class="score-label">Predicted Probability of<br>Endometriosis Compared<br>to Surgical Controls<br>(100% probability)</div>
      <div class="score-value">
        <span class="score-figure">38.7%</span>
        <svg width="52" height="52" viewBox="0 0 52 52" role="img" aria-label="38.7 percent ring gauge">
          <circle cx="26" cy="26" r="22" fill="none" stroke="var(--ring-dark)" stroke-width="6"/>
          <circle cx="26" cy="26" r="22" fill="none" stroke="var(--ring-accent)" stroke-width="6"
            stroke-dasharray="53.5 138.2" transform="rotate(-5 26 26)"/>
        </svg>
      </div>
    </section>

    <div class="range-heading">Reference Range</div>

    <table class="range-table">
      <tr><td class="band">1.0.0-29.9%</td><td>- low probability of endometriosis</td></tr>
      <tr class="inconclusive"><td class="band">2.29.9-44.9%</td><td>- inconclusive</td></tr>
      <tr><td class="band">3.45.o-55.0%</td><td>- intermediate risk of endometriosis</td></tr>
      <tr><td class="band">4.55.1-64.9%</td><td>- probable endometriosis</td></tr>
      <tr class="high"><td class="band">65.0-99.9%</td><td>- highly probable endometriosis</td></tr>
    </table>
  </main>
</body>
</html>
```